Northlake Imaging Partners
Professional
DMS, RDCS
418 Pellwick Row
Brenmoor, CA 93417
tvasquell@northlakeimagingpartners.com
www.northlakeimagingpartners.com
Providing high quality ultrasound imaging service in the convenience of the Physician's office.
Increase in quality patient care.
Full body ultrasound 7 days a week
High qulity equipment
Professional staff
Quick turnearound
Your Diagnostic Imaging Specialist
Logo file for NIP stationary

```html
<!DOCTYPE html>
<html lang="en">
<head>
<meta charset="utf-8">
<title>Northlake Imaging Partners – Business Cards</title>
<link href="https://fonts.googleapis.com/css2?family=PT+Sans:wght@400;700&display=swap" rel="stylesheet">
<style>
  :root{
    --bg:#ecebe8;
    --purple:#8c4e99;
    --purple-dark:#6f3a7c;
    --purple-light:#a56bb0;
    --grey:#555a5f;
    --grey-light:#b9b9bd;
    --card:#ffffff;
    --ink:#3c3c3c;
  }
  *{margin:0;padding:0;box-sizing:border-box}
  html,body{width:1200px;height:911px;overflow:hidden}
  body{background:var(--bg);font-family:"PT Sans",Arial,sans-serif;position:relative}
  .card{position:absolute;width:420px;height:240px;border-radius:10px;overflow:hidden;
    box-shadow:0 4px 14px rgba(0,0,0,.18)}
  .card--front{left:143px;top:296px;background:var(--card)}
  .card--back{left:630px;top:210px;background:linear-gradient(135deg,var(--purple-light),var(--purple-dark))}
  .card--plain{left:363px;top:514px;background:linear-gradient(160deg,#ffffff,#f1f0f2)}
  .card__band{position:absolute;left:0;top:0;width:420px;height:110px}
  .brand{position:absolute;display:flex;align-items:center;gap:8px}
  .brand__mark{width:26px;height:26px;border-radius:50%;background:var(--purple);flex:none}
  .brand__name{font-weight:700;line-height:1;text-transform:uppercase}
  .brand__main{display:block;font-size:22px;color:var(--purple);white-space:nowrap}
  .brand__sub{display:block;font-size:13px;color:var(--grey);text-align:right;margin-top:2px}
  .card--front .brand{left:22px;top:98px}
  .card--back .brand{right:22px;bottom:26px;display:block;text-align:right}
  .card--back .brand__main,.card--back .brand__sub{color:#fff}
  .card--plain .brand{right:22px;bottom:26px;display:block;text-align:right}
  .card--plain .brand__sub{color:var(--grey)}
  .faint-emblem{position:absolute;border-radius:50%}
  .card--back .faint-emblem{left:20px;top:10px;width:170px;height:170px;background:radial-gradient(circle,rgba(255,255,255,.22),rgba(255,255,255,0) 70%)}
  .card--plain .faint-emblem{left:20px;top:6px;width:170px;height:170px;background:radial-gradient(circle,rgba(140,78,153,.14),rgba(140,78,153,0) 70%)}
  .contact{position:absolute;left:92px;top:162px;font-size:8.5px;color:var(--ink);line-height:1.5}
  .contact__address{margin-bottom:9px}
  .contact__row{display:flex;gap:10px}
  .contact__col{padding-right:10px}
  .contact__col + .contact__col{border-left:1px solid var(--grey-light);padding-left:10px;padding-right:0}
</style>
</head>
<body>
  <section class="card card--front" aria-label="Business card front">
    <svg class="card__band" viewBox="0 0 420 110" aria-hidden="true">
      <defs>
        <linearGradient id="bandPurple" x1="0" y1="0" x2="1" y2="0">
          <stop offset="0" stop-color="#9a5ca6"/>
          <stop offset="1" stop-color="#7a4287"/>
        </linearGradient>
      </defs>
      <path d="M0 0H420V62C330 22 220 22 0 54Z" fill="url(#bandPurple)"/>
      <path d="M0 54C220 22 330 22 420 62V86C330 38 230 36 0 62Z" fill="#4d4f53"/>
      <path d="M0 62C230 36 330 38 420 86V92C330 48 230 46 0 68Z" fill="#c6c6ca"/>
    </svg>
    <div class="brand">
      <span class="brand__mark"></span>
      <span class="brand__name">
        <span class="brand__main">Northlake Imaging</span>
        <span class="brand__sub">Partners</span>
      </span>
    </div>
    <div class="contact">
      <p class="contact__address">418 Pellwick Row, Brenmoor, CA 93417</p>
      <div class="contact__row">
        <div class="contact__col">
          <p>P: 358-555-0142</p>
          <p>F: 358-555-0187</p>
        </div>
        <div class="contact__col">
          <p>E: tvasquell@northlakeimagingpartners.com</p>
          <p>W: www.northlakeimagingpartners.com</p>
        </div>
      </div>
    </div>
  </section>

  <section class="card card--back" aria-label="Business card back, purple">
    <div class="faint-emblem" role="img" aria-label="Faint brand emblem area"></div>
    <div class="brand">
      <span class="brand__name">
        <span class="brand__main">Northlake Imaging</span>
        <span class="brand__sub">Partners</span>
      </span>
    </div>
  </section>

  <section class="card card--plain" aria-label="Business card back, white">
    <div class="faint-emblem" role="img" aria-label="Faint brand emblem area"></div>
    <div class="brand">
      <span class="brand__name">
        <span class="brand__main">Northlake Imaging</span>
        <span class="brand__sub">Partners</span>
      </span>
    </div>
  </section>
</body>
</html>
```